Tri fold brochure for construction company

Looking for a tri fold brochure which utilizes black, teal and white colors. Logo must be on main page (several files with Logo attached)
Inside brochure.
1st Page - 3D photo/sketch/drawing of a complete residential high rise building with windows, balconies and elements of concrete and bricks.
2nd Page - Text which will outline company's main activities. file with text is attached.
3rd Page - photo/sketch/drawing of underground parking garage which shows columns/beams/walls/ and garage entrance/exit ramp. Can be multiple photos.
Back of brochure
1st page - company logo
2nd page - please propose something.
3rd page - company message with address and contact info (to be provided)
Back ground color of brochure should complement our logo/photos/sketches/drawings.
Alternative design options are welcome.

```html
<!DOCTYPE html>
<html lang="en">
<head>
<meta charset="utf-8">
<title>Meridian Restoration Corp. – Tri-fold Brochure</title>
<link href="https://fonts.googleapis.com/css2?family=Ubuntu:wght@500;700&family=Lato:wght@400;700&display=swap" rel="stylesheet">
<style>
  :root{
    --teal:#26a58a;
    --teal-deep:#1f8f78;
    --ink:#2b2b2b;
    --white:#ffffff;
    --stripe:#e9e9e9;
    --stage:#6a6a6a;
    --quote-grey:#8e8e8e;
    --sky:#b4cde2;
    --city-top:#cfd8e1;
    --city-low:#7e8da1;
  }
  *{margin:0;padding:0;box-sizing:border-box}
  html,body{width:837px;height:1200px;overflow:hidden}
  body{background:var(--stage);position:relative;font-family:"Lato",sans-serif;color:var(--white)}
  .spread{position:absolute;left:65px;width:709px;height:501px;overflow:hidden;background:var(--teal)}
  .spread--outside{top:71px}
  .spread--inside{top:636px}
  .spread svg.art{position:absolute;inset:0;width:709px;height:501px}
  .abs{position:absolute}

  /* outside */
  .quote{width:175px;font-size:8.4px;line-height:11.4px}
  .quote__mark{font-family:"Ubuntu",sans-serif;font-weight:700;font-size:46px;line-height:30px;height:26px}
  .quote p{margin-top:8px}
  .quote__foot{display:flex;justify-content:flex-end;align-items:flex-start;gap:6px;margin-top:6px}
  .quote__by{font-weight:700;font-size:6.6px;line-height:10px}
  .quote__foot .quote__mark{height:24px}
  .quote--sky{color:var(--ink)}
  .quote--sky .quote__mark{color:var(--quote-grey)}
  .quote--teal .quote__mark{color:var(--white)}
  .site{width:236px;text-align:center;font-size:10px}
  .site b{font-weight:700}
  .contact{width:236px;text-align:center;font-size:8.4px;line-height:11.5px}
  .contact h3{font-family:"Ubuntu",sans-serif;font-weight:700;font-size:14px;margin-bottom:6px}
  .rule{display:block;width:16px;height:3px;background:var(--white);border-radius:2px;margin:0 auto 8px}
  .contact p{margin-bottom:6px}
  .contact svg{width:8px;height:8px;vertical-align:-1px;margin-right:3px}
  .brand{width:236px;text-align:center;color:var(--ink)}
  .brand__mark{display:block;width:24px;height:24px;background:var(--teal);margin:0 auto 14px}
  .brand__name{font-family:"Ubuntu",sans-serif;font-weight:700;font-size:21px;letter-spacing:.5px;line-height:24px}
  .brand__sub{font-family:"Ubuntu",sans-serif;font-weight:700;font-size:9px;letter-spacing:.5px;display:block;margin-top:2px;color:var(--teal)}
  .headline{width:236px;text-align:center;font-family:"Ubuntu",sans-serif;font-weight:700;font-size:13.2px;line-height:17px}
  .headline .rule{margin-top:6px}

  /* inside */
  .services{font-size:8.8px;line-height:11.5px}
  .services--left{width:190px}
  .services--right{width:176px}
  .services h2{font-family:"Ubuntu",sans-serif;font-weight:700;font-size:15.5px;line-height:17px}
  .services .rule{margin:7px 0 9px}
  .services h3{font-family:"Ubuntu",sans-serif;font-weight:500;font-size:10.5px;margin:7px 0 4px}
  .services ul{list-style:none}
  .services li{padding-left:10px;position:relative}
  .services li::before{content:"✓";position:absolute;left:0}
  .photo-apartments{clip-path:polygon(0 48px,100% 26px,100% 100%,0 100%);background:linear-gradient(180deg,#a9c6e3 0%,#c8874f 45%,#8a6b4e 75%,#8fa35a 100%)}
  .placeholder-helmet{background:rgba(255,255,255,.18)}
</style>
</head>
<body>

<section class="spread spread--outside" aria-label="Brochure outside">
  <svg class="art" viewBox="0 0 709 501" aria-hidden="true">
    <defs>
      <linearGradient id="cityTone" x1="0" y1="0" x2="0" y2="1">
        <stop offset="0" stop-color="var(--city-top)"/>
        <stop offset="1" stop-color="var(--city-low)"/>
      </linearGradient>
    </defs>
    <polygon points="0,0 473,0 473,352 0,283" fill="url(#cityTone)"/>
    <polygon points="0,283 473,352 473,362 0,322" fill="var(--ink)"/>
    <polygon points="473,0 709,0 709,397 473,366" fill="var(--sky)"/>
    <polygon points="473,366 709,397 709,408 473,378" fill="var(--ink)"/>
  </svg>
  <div class="abs" role="img" aria-label="Photo of a city skyline with high-rise towers" style="left:0;top:0;width:473px;height:300px"></div>
  <div class="abs" role="img" aria-label="Photo looking up at glass skyscrapers against the sky" style="left:473px;top:150px;width:236px;height:215px"></div>

  <div class="abs quote quote--sky" style="left:31px;top:29px">
    <div class="quote__mark">“</div>
    <p>Lorem ipsum dolor sit amet, consectetur adipiscing elit, sed do eiusmod tempor incididunt ut labore et dolore magna aliqua.</p>
    <div class="quote__foot"><span class="quote__by">Lorem ipsum dolor</span><span class="quote__mark">”</span></div>
  </div>

  <div class="abs quote quote--teal" style="left:31px;top:360px">
    <div class="quote__mark">“</div>
    <p>Lorem ipsum dolor sit amet, consectetur adipiscing elit, sed do eiusmod tempor incididunt ut labore et dolore magna aliqua.</p>
    <div class="quote__foot"><span class="quote__by">Lorem ipsum dolor</span><span class="quote__mark">”</span></div>
  </div>

  <div class="abs contact" style="left:236px;top:380px">
    <h3>Contact Us</h3>
    <span class="rule"></span>
    <p><svg viewBox="0 0 10 10"><path d="M5 1a3 3 0 0 1 3 3c0 2-3 5-3 5S2 6 2 4a3 3 0 0 1 3-3z" fill="none" stroke="#fff"/></svg>Address line 1, Address line 1<br>Address line 1</p>
    <p><svg viewBox="0 0 10 10"><rect x="1" y="2" width="8" height="6" fill="none" stroke="#fff"/><path d="M1 2l4 3 4-3" fill="none" stroke="#fff"/></svg>info@yourmail.com</p>
    <p><svg viewBox="0 0 10 10"><circle cx="5" cy="5" r="4" fill="none" stroke="#fff"/><path d="M3.5 3.5l1 1-0.5 1 1 1 1-0.5 1 1" fill="none" stroke="#fff"/></svg>0123 456 789</p>
  </div>

  <div class="abs brand" style="left:473px;top:72px">
    <span class="brand__mark"></span>
    <div class="brand__name">MERIDIAN</div>
    <span class="brand__sub">RESTORATION CORP.</span>
  </div>

  <div class="abs headline" style="left:473px;top:427px">
    LOREM IPSUM DOLOR<br>SIT AMET, CONSECTETUR
    <span class="rule"></span>
  </div>

  <div class="abs site" style="left:0;top:474px">www.<b>MeridianRestoration</b>.com</div>
  <div class="abs site" style="left:236px;top:474px">www.<b>MeridianRestoration</b>.com</div>
  <div class="abs site" style="left:473px;top:474px">www.<b>MeridianRestoration</b>.com</div>
</section>

<section class="spread spread--inside" aria-label="Brochure inside">
  <svg class="art" viewBox="0 0 709 501" aria-hidden="true">
    <rect x="380" y="80" width="329" height="400" fill="var(--teal-deep)" opacity=".35"/>
    <polygon points="0,0 436,0 0,40" fill="var(--ink)"/>
    <polygon points="0,40 436,0 480,0 0,48" fill="var(--stripe)"/>
    <polygon points="236,501 709,420 709,440 300,501" fill="var(--white)"/>
    <polygon points="300,501 709,440 709,501" fill="var(--ink)"/>
  </svg>
  <div class="abs photo-apartments" role="img" aria-label="Photo of a colourful residential apartment building with balconies and a playground" style="left:0;top:0;width:236px;height:501px"></div>
  <div class="abs" role="img" aria-label="Faint city skyline behind the service lists" style="left:380px;top:80px;width:329px;height:340px"></div>
  <div class="abs placeholder-helmet" role="img" aria-label="Photo of a yellow safety hard hat" style="left:546px;top:368px;width:135px;height:116px"></div>

  <div class="abs services services--left" style="left:270px;top:33px">
    <h2>Building Envelope:</h2>
    <span class="rule"></span>
    <h3>Concrete repairs</h3>
    <ul><li>Balcony slabs</li><li>Shear Walls</li><li>Beams &amp; Columns</li></ul>
    <h3>Masonry repairs</h3>
    <ul><li>Brick, Block &amp; Stone replacement</li><li>Tuck pointing</li><li>Through wall flashing</li><li>Coating (Sealer, Elastomeric, Silicone and Architectural coatings)</li></ul>
    <h3>Sealant Replacement</h3>
    <ul><li>Window wall and glazing system sealants</li><li>Precast sealants</li><li>Masonry sealants</li><li>Balcony perimeter joints</li></ul>
    <h3>Waterproofing</h3>
    <ul><li>Balconies &amp; Terraces thin system</li><li>Garbage &amp; Mechanical rooms</li></ul>
    <h2 style="margin-top:14px">Parking<br>Garage Structures:</h2>
    <span class="rule" style="margin:6px 0 7px"></span>
    <h3>Concrete repairs</h3>
    <ul><li>Partial slab replacement</li><li>Top/under side repairs</li><li>Hydro demolition</li><li>Columns, Beams and Shear Walls</li><li>Catch basins &amp; trench drains</li><li>Staircases</li></ul>
  </div>

  <div class="abs services services--right" style="left:504px;top:33px">
    <h3 style="margin-top:0">Waterproofing</h3>
    <ul><li>Vehicular thin system (drive aisles, parking bays, ramps, etc.)</li><li>Hot applied waterproofing (Ramps and Roof decks)</li><li>Expansion joints repairs/replacement</li><li>Mastic waterproofing system</li><li>Foundation wall crack injections</li><li>Crystalline waterproofing</li></ul>
    <h3 style="margin-top:14px">Ramp Remediation</h3>
    <ul><li>Electric heating cables</li><li>Asphalt, Interlocking, Mastic and Concrete</li></ul>
    <h2 style="margin-top:22px">Miscellaneous</h2>
    <span class="rule"></span>
    <ul><li>Railings remediation and replacement</li><li>Outside garbage pad enclosures</li><li>Retaining walls repair/replacement</li><li>Weeping tile systems</li><li>Safety bollards &amp; precast curbs installation</li><li>Side walks, curbs, interlocking, asphalt and concrete pads</li><li>Balconies and Parking garages painting</li><li>Area drains replacements</li><li>Etc.</li></ul>
  </div>
</section>

</body>
</html>
```